Teach English in China Website Redesign Needed

We recruit native English speakers from the US, UK, etc. who want to teach English as a foreign language in schools in China. Our target customer is college educated, age 22-28 and they love to travel. We prefer designs with bright colors and lots of photos. We want to keep all the text on our current homepage, LanternClassroomHub.com. We are open to changing our logo. A competitor's page that we like is bluepeakmentors.com because of their bright colors, photos and use of white space. We are happy to give you a dofollow link and design credit on our homepage. The use of included photos is optional. We need at least a home page design and a standard blog post design.
Target Market(s)
Our target customer is college educated, age 22-28 and they love to travel. Half of our customers are kindergarten teachers. Half of our customers are male.
Logo Text
Lantern Classroom Hub
Number of Pages Required
2 page
Requirements
Must have
- Bright colors
Should not have
- Our homepage must not look crowded. Use white space effectively.

```html
<!DOCTYPE html>
<html lang="en">
<head>
<meta charset="utf-8">
<title>Lantern Classroom Hub – Teach English in China</title>
<link href="https://fonts.googleapis.com/css2?family=Open+Sans:wght@400;600;700&family=Ubuntu:wght@400;500;700&display=swap" rel="stylesheet">
<style>
:root{
  --red:#e0141e;
  --red-dark:#c10d17;
  --yellow:#f6b515;
  --green:#8dc63f;
  --ink:#222;
  --text:#666;
  --muted:#999;
  --grey-band:#ececec;
  --charcoal:#2d2d30;
  --footer:#2a2a2a;
  --line:#e2e2e2;
  --white:#fff;
}
*{margin:0;padding:0;box-sizing:border-box}
html,body{width:1200px;height:4128px;overflow:hidden}
body{position:relative;background:var(--white);font-family:"Open Sans",Arial,sans-serif;color:var(--text)}
.abs{position:absolute}
h1,h2,h3,h4{font-family:"Ubuntu","Open Sans",sans-serif;font-weight:400}

/* header */
.site-header{left:0;top:0;width:1200px;height:110px;background:var(--white)}
.brand{left:118px;top:28px;font-family:"Ubuntu",sans-serif;font-weight:700;font-size:27px;line-height:32px;color:var(--ink);width:260px}
.brand-dot{display:inline-block;width:12px;height:12px;border-radius:50%;background:var(--red);margin-right:8px;vertical-align:2px}
.social{right:130px;top:28px;display:flex;gap:8px}
.social span{width:24px;height:24px;border-radius:50%;background:#111}
.main-nav{left:494px;top:67px;display:flex;gap:0;font-size:13px;color:#444;font-weight:600;letter-spacing:.2px}
.main-nav a{color:inherit;text-decoration:none;margin-right:42px;padding-bottom:10px}
.main-nav a.active{color:var(--red);border-bottom:2px solid var(--red)}

/* hero */
.hero-band{left:0;top:110px;width:1200px;height:523px;background:var(--grey-band)}
.hero-photo{left:118px;top:146px;width:964px;height:437px;background:linear-gradient(120deg,#f3c94a 0%,#f5e7c4 35%,#efe3d2 60%,#d7b58c 85%,#a3753f 100%)}
.hero-caption{left:660px;top:352px;width:367px;height:50px;background:rgba(30,30,30,.85);color:var(--white);font-family:"Ubuntu",sans-serif;font-size:23px;line-height:50px;text-align:center;letter-spacing:.5px}
.hero-dots{left:566px;top:560px;display:flex;gap:8px}
.hero-dots span{width:10px;height:10px;border-radius:50%;background:rgba(255,255,255,.7)}

/* intro */
.intro-title{left:0;top:680px;width:1200px;text-align:center;font-size:31px;color:var(--ink);letter-spacing:.5px}
.title-rule{width:40px;height:2px;background:var(--red)}
.intro-text{left:160px;top:760px;width:880px;text-align:center;font-size:13.2px;line-height:24px;color:var(--text)}
.feature{top:908px;height:149px;color:var(--white);padding:22px 22px}
.feature h3{font-size:22px;font-weight:700;margin-bottom:8px}
.feature p{font-size:12px;line-height:17px;width:200px;opacity:.95}
.feature svg{position:absolute;right:14px;bottom:12px}
.feature--red{left:179px;width:261px;background:var(--red)}
.feature--yellow{left:460px;width:267px;background:var(--yellow)}
.feature--green{left:743px;width:264px;background:var(--green)}

/* highlights */
.highlights{left:0;top:1109px;width:1200px;height:410px;background:var(--charcoal)}
.hl-frame{left:158px;top:1164px;width:212px;height:281px;background:var(--red)}
.hl-photo{left:118px;top:1200px;width:322px;height:210px;background:linear-gradient(160deg,#9aa0a8 0%,#5a5f68 40%,#c9c3bb 70%,#3a3a40 100%);border:5px solid var(--white)}
.hl-title{left:468px;top:1160px;font-size:31px;color:var(--white);letter-spacing:.5px}
.hl-list{left:468px;top:1212px;width:640px;list-style:none;color:#ddd;font-size:13.4px;line-height:21px}
.hl-list li{position:relative;padding-left:22px}
.hl-list li::before{content:"";position:absolute;left:2px;top:6px;width:9px;height:9px;border-radius:50%;background:var(--red)}

/* testimonials */
.testi-title{left:0;top:1615px;width:1200px;text-align:center;font-size:35px;color:var(--ink)}
.testi-sub{left:0;top:1668px;width:1200px;text-align:center;font-size:13.5px;color:var(--red)}
.avatar{width:83px;height:83px}
.avatar--one{left:132px;top:1761px;background:linear-gradient(135deg,#c9a27a,#6e5a48)}
.avatar--two{left:638px;top:1761px;background:linear-gradient(180deg,#e6e6e6,#bdbdbd)}
.person{width:170px;text-align:center}
.person b{display:block;font-size:13px;color:var(--ink);font-weight:600}
.person small{display:block;font-size:11px;font-style:italic;color:var(--muted);margin-top:4px}
.quote{width:290px;font-size:12px;line-height:18px;color:var(--text);text-align:center}
.quote::before{content:"\201C";position:absolute;left:-8px;top:-8px;font-size:26px;color:#333;font-family:Georgia,serif}
.quote::after{content:"\201D";font-size:20px;color:#333;font-family:Georgia,serif;vertical-align:-6px;margin-left:4px}

/* faq */
.faq-panel{left:0;top:1960px;width:586px;height:476px;background:var(--red)}
.faq-photo{left:586px;top:1960px;width:614px;height:476px;background:linear-gradient(135deg,#6d4a30 0%,#a2764c 30%,#7fc7e6 55%,#d6b08a 75%,#4e3724 100%)}
.faq-title{left:118px;top:1995px;font-size:38px;color:var(--white)}
.faq-sub{left:118px;top:2045px;font-size:13.5px;color:var(--white)}
.faq-item{left:118px;width:438px;border:1.5px solid rgba(255,255,255,.85);color:var(--white);font-size:13px;font-weight:700;padding:0 14px;line-height:36px}
.faq-item svg{position:absolute;right:12px;top:13px}
.faq-item p{font-weight:600;font-size:12.5px;line-height:19px;padding-bottom:10px}

/* blog */
.blog-title{left:0;top:2505px;width:1200px;text-align:center;font-size:42px;color:var(--ink)}
.blog-sub{left:0;top:2570px;width:1200px;text-align:center;font-size:14px;color:var(--text)}
.blog-divider{left:118px;top:2620px;width:964px;height:1px;background:var(--line)}
.blog-notch{left:588px;top:2612px;width:16px;height:16px;background:var(--white);border-right:1px solid var(--line);border-bottom:1px solid var(--line);transform:rotate(45deg)}
.card{top:2683px;height:350px;background:var(--white);box-shadow:0 1px 4px rgba(0,0,0,.18)}
.card--a{left:157px;width:270px}
.card--b{left:449px;width:269px}
.card--c{left:738px;width:269px}
.card-img{height:165px}
.card-img--a{background:linear-gradient(135deg,#e8d9b8,#9a8a6a 50%,#d4c7a5)}
.card-img--b{background:linear-gradient(180deg,#a9c6df 0%,#e9eef2 55%,#8b7a67 100%)}
.card-img--c{background:linear-gradient(135deg,#f2f2f2,#c9d6e6 50%,#e9b9b0)}
.card-tag{position:absolute;right:12px;top:160px;width:26px;height:14px;background:var(--red)}
.card-tag-box{position:absolute;right:12px;top:174px;width:26px;height:20px;border:1px solid var(--line)}
.card h4{padding:30px 16px 0;font-size:14px;color:var(--ink);font-family:"Open Sans",sans-serif;font-weight:400}
.card p{padding:12px 16px 0;font-size:11px;line-height:15px;color:var(--muted)}
.card-meta{position:absolute;left:0;bottom:0;width:100%;height:36px;border-top:1px solid var(--line);font-size:10.5px;color:var(--muted);line-height:36px;padding:0 16px}
.card-meta span{margin-right:16px}
.card-meta svg{position:absolute;right:14px;top:13px}
.slider-dots{left:544px;top:3070px;display:flex;gap:8px}
.slider-dots span{width:12px;height:12px;border-radius:50%;border:1.5px solid #bbb}
.slider-dots span.on{background:var(--red);border-color:var(--red)}

/* apply */
.apply-bg{left:0;top:3159px;width:1200px;height:543px;background:linear-gradient(120deg,#5c7c8c 0%,#9a6a4c 35%,#c46b4b 55%,#8a9baa 75%,#4a5660 100%)}
.apply-panel{left:182px;top:3225px;width:803px;height:413px;background:rgba(30,30,32,.9)}
.apply-title{left:212px;top:3255px;font-size:31px;font-weight:700;color:var(--white)}
.apply-sub{left:212px;top:3297px;font-size:14px;color:#ddd}
.field{height:28px;background:var(--white);font-size:11.5px;color:#888;line-height:28px;padding:0 8px}
.col1{left:206px;width:229px}.col2{left:462px;width:234px}.col3{left:721px;width:231px}
.textarea{left:206px;top:3476px;width:746px;height:66px;line-height:20px;padding-top:6px}
.send-btn{left:405px;top:3575px;width:377px;height:46px;background:var(--red);color:var(--white);font-weight:700;font-size:15px;line-height:46px;text-align:center}

/* footer */
.site-footer{left:0;top:3702px;width:1200px;height:426px;background:var(--footer)}
.f-head{top:3780px;font-size:14px;font-weight:700;color:var(--white);font-family:"Open Sans",sans-serif}
.f-rule{top:3806px;width:40px;height:2px;background:var(--red)}
.f-text{font-size:12px;line-height:20px;color:#777}
.f-links{font-size:12px;line-height:30px;color:#bbb;list-style:none}
.f-links li.on{color:var(--white);font-weight:600}
.course-thumb{width:55px;height:55px}
.course b{display:block;font-size:12px;color:#ddd;font-weight:600}
.course small{display:block;font-size:10.5px;line-height:15px;color:#777}
.f-input{left:845px;width:218px;border:1px solid #444;background:#2f2f2f;font-size:11.5px;color:#888;padding:0 10px}
.f-send{left:1030px;top:3974px;width:33px;height:26px;background:var(--red)}
.f-bottom{left:0;top:4082px;width:1200px;height:46px;border-top:1px solid #3a3a3a}
.copyright{left:118px;top:4095px;font-size:11.5px;color:#777}
</style>
</head>
<body>

<header class="site-header abs">
  <div class="brand abs"><span class="brand-dot"></span>Lantern Classroom Hub</div>
  <div class="social abs" aria-label="Social links"><span></span><span></span><span></span><span></span><span></span></div>
  <nav class="main-nav abs">
    <a class="active">HOME</a><a>AVAILABLE JOBS</a><a>APPLY ONLINE</a><a>BLOG</a><a>FAQ</a><a>CONTACT</a>
  </nav>
</header>

<section class="hero">
  <div class="hero-band abs"></div>
  <div class="hero-photo abs" role="img" aria-label="Photo of a smiling teacher helping young children at a classroom table"></div>
  <div class="hero-caption abs">TEACH ENGLISH IN CHINA</div>
  <div class="hero-dots abs"><span></span><span></span><span></span></div>
</section>

<section class="intro">
  <h2 class="intro-title abs">TEACH ENGLISH IN CHINA</h2>
  <div class="title-rule abs" style="left:580px;top:732px"></div>
  <p class="intro-text abs">Want to teach English in China? Do you enjoy teaching children or adults? Would you like the adventure of teaching in China for a year? Then we have the perfect job for you! We are seeking English speakers from the US, UK, Canada, Ireland, Australia, New Zealand and South Africa to teach English in China for a year (or longer if you wish). We recruit for hundreds of schools all over China such as Bright Path English, Harbor Street English, Willow Lane English, Maple Road English, Sunny Steps, Oakridge Kids, Golden Pear, public schools, international schools, universities, and more.</p>

  <div class="feature feature--red abs">
    <h3>Available Job</h3>
    <p>Lorem Ipsum is simply dummy text of the typesetting when an unknown printer and scrambled.</p>
    <svg width="44" height="44" viewBox="0 0 44 44" fill="none" stroke="rgba(255,255,255,.45)" stroke-width="3"><circle cx="18" cy="18" r="12"/><path d="M27 27l13 13"/></svg>
  </div>
  <div class="feature feature--yellow abs">
    <h3>Required</h3>
    <p>Lorem Ipsum is simply dummy text of the typesetting when an unknown printer and scrambled.</p>
    <svg width="44" height="44" viewBox="0 0 44 44" fill="none" stroke="rgba(255,255,255,.45)" stroke-width="3"><rect x="4" y="10" width="28" height="30"/><path d="M20 28l16-22 5 4-16 22-7 3z"/></svg>
  </div>
  <div class="feature feature--green abs">
    <h3>We Offer</h3>
    <p>Lorem Ipsum is simply dummy text of the typesetting when an unknown printer and scrambled.</p>
    <svg width="44" height="44" viewBox="0 0 44 44" fill="none" stroke="rgba(255,255,255,.45)" stroke-width="3"><rect x="8" y="4" width="30" height="36"/><path d="M14 14h18M14 22h18M14 30h12"/></svg>
  </div>
</section>

<section class="highlights abs"></section>
<div class="hl-frame abs"></div>
<div class="hl-photo abs" role="img" aria-label="Group photo of smiling students and a teacher"></div>
<h2 class="hl-title abs">HIGHLIGHTS</h2>
<ul class="hl-list abs">
  <li>Competitive compensation: 7000-9000 RMB/month, up to 18,000 RMB (divide by 6.5 for US dollars) if you have a bachelor's degree, 2+ years of teaching experience</li>
  <li>Housing allowance: 2000 RMB/month (housing is cheaper in China)</li>
  <li>Teach private English lessons after work for 250 RMB/hr ($38 US per hour)</li>
  <li>Airfare reimbursement: 5000 RMB at end of completed 1 year contract</li>
  <li>Free TESOL / TEFL training and certification</li>
  <li>Invitation letter so you can apply for a visa (Z if you have a bachelor's degree).</li>
  <li>Airport pickup</li>
  <li>5-day work week, 25 hours teaching per week plus some office hours</li>
  <li>20 paid holidays</li>
  <li>Free Chinese classes 2 hours per week with most jobs</li>
</ul>

<section class="testimonials">
  <h2 class="testi-title abs">WHAT OUR USERS ARE SAYING</h2>
  <p class="testi-sub abs">Find out why our users keep using Lantern Classroom Hub</p>

  <div class="avatar avatar--one abs" role="img" aria-label="Portrait photo of a reviewer"></div>
  <div class="person abs" style="left:89px;top:1850px"><b>Daniel Reyes</b><small>CEO - Company Name</small></div>
  <p class="quote abs" style="left:286px;top:1770px">The services Testimonials provides are marvelous. The support is fast and helpful. This Testimonial Slider helps increase customers and provide them safety and more information about your product through existing users.</p>

  <div class="avatar avatar--two abs" role="img" aria-label="Placeholder portrait of a reviewer"></div>
  <div class="person abs" style="left:595px;top:1850px"><b>Samir Khan</b><small>Dev - Brightnote Studio</small></div>
  <p class="quote abs" style="left:785px;top:1770px">The services Testimonials provides are marvelous. The support is fast and helpful. This Testimonial Slider helps increase customers and provide them safety and more information about your product through existing users.</p>
</section>

<section class="faq">
  <div class="faq-panel abs"></div>
  <div class="faq-photo abs" role="img" aria-label="Photo of a smiling student holding books in a library"></div>
  <h2 class="faq-title abs">FAQ</h2>
  <p class="faq-sub abs">Read frequently asked questions about our program.</p>
  <div class="faq-item abs" style="top:2086px">I can't speak Chinese. Is that a problem?
    <svg width="8" height="10" viewBox="0 0 8 10"><path d="M1 1l5 4-5 4" fill="none" stroke="#fff" stroke-width="2"/></svg></div>
  <div class="faq-item abs" style="top:2141px">Where in China do you place teachers and in what schools?
    <svg width="8" height="10" viewBox="0 0 8 10"><path d="M1 1l5 4-5 4" fill="none" stroke="#fff" stroke-width="2"/></svg></div>
  <div class="faq-item abs" style="top:2194px">What's the next step after my video call interview?
    <svg width="10" height="8" viewBox="0 0 10 8"><path d="M1 1l4 5 4-5" fill="none" stroke="#fff" stroke-width="2"/></svg>
    <p>We take excellent care of our teachers. Though we are paid by the schools we send teachers to, our number one priority is our teachers. We know what different schools are looking for and can quickly match you up with a school that will appreciate what you have to offer.</p></div>
  <div class="faq-item abs" style="top:2336px">Will I have enough money to support myself?
    <svg width="8" height="10" viewBox="0 0 8 10"><path d="M1 1l5 4-5 4" fill="none" stroke="#fff" stroke-width="2"/></svg></div>
</section>

<section class="blog">
  <h2 class="blog-title abs">Blog Posts</h2>
  <p class="blog-sub abs">Check out popular activities and hobby classes</p>
  <div class="blog-divider abs"></div>
  <div class="blog-notch abs"></div>

  <article class="card card--a abs">
    <div class="card-img card-img--a" role="img" aria-label="Photo of a man working on a laptop"></div>
    <span class="card-tag"></span><span class="card-tag-box"></span>
    <h4>Internet Entrepreneurship</h4>
    <p>Lorem ipsum dolor sit amet, consectetur adipisicing elit, sed do eiusmod tempor incididunt ut labore et dolore magna aliqua.</p>
    <div class="card-meta"><span>5 lessons</span><span>Beginner</span>
      <svg width="10" height="10" viewBox="0 0 10 10" fill="#999"><circle cx="2" cy="5" r="1.5"/><circle cx="8" cy="2" r="1.5"/><circle cx="8" cy="8" r="1.5"/><path d="M2 5L8 2M2 5l6 3" stroke="#999"/></svg></div>
  </article>
  <article class="card card--b abs">
    <div class="card-img card-img--b" role="img" aria-label="Photo of a person sitting on a wooden deck under a sky with a balloon"></div>
    <span class="card-tag"></span><span class="card-tag-box"></span>
    <h4>DIY-Stencil Painting on Bag</h4>
    <p>Lorem ipsum dolor sit amet, consectetur adipisicing elit, sed do eiusmod tempor incididunt ut labore et dolore magna aliqua.</p>
    <div class="card-meta"><span>Advanced</span>
      <svg width="10" height="10" viewBox="0 0 10 10" fill="#999"><circle cx="2" cy="5" r="1.5"/><circle cx="8" cy="2" r="1.5"/><circle cx="8" cy="8" r="1.5"/><path d="M2 5L8 2M2 5l6 3" stroke="#999"/></svg></div>
  </article>
  <article class="card card--c abs">
    <div class="card-img card-img--c" role="img" aria-label="Photo of charts and a tablet on a desk"></div>
    <span class="card-tag"></span><span class="card-tag-box"></span>
    <h4>Kids and Healthy Eating habits</h4>
    <p>Lorem ipsum dolor sit amet, consectetur adipisicing elit, sed do eiusmod tempor incididunt ut labore et dolore magna aliqua.</p>
    <div class="card-meta"><span>2 lessons</span><span>Intermediate</span>
      <svg width="10" height="10" viewBox="0 0 10 10" fill="#999"><circle cx="2" cy="5" r="1.5"/><circle cx="8" cy="2" r="1.5"/><circle cx="8" cy="8" r="1.5"/><path d="M2 5L8 2M2 5l6 3" stroke="#999"/></svg></div>
  </article>
  <div class="slider-dots abs"><span class="on"></span><span></span><span></span><span></span></div>
</section>

<section class="apply">
  <div class="apply-bg abs" role="img" aria-label="Photo of a bright classroom full of students"></div>
  <div class="apply-panel abs"></div>
  <h2 class="apply-title abs">Apply Now</h2>
  <p class="apply-sub abs">Fill out our short form and upload your resume.</p>
  <div class="field col1 abs" style="top:3337px">Your First and Last Name</div>
  <div class="field col2 abs" style="top:3337px">Your Email</div>
  <div class="field col3 abs" style="top:3337px">The time zone you're in</div>
  <div class="field col1 abs" style="top:3381px">Phone</div>
  <div class="field col2 abs" style="top:3381px">Video chat ID</div>
  <div class="field col3 abs" style="top:3381px">The time zone you're in</div>
  <div class="field col1 abs" style="top:3427px">Your Birthdate</div>
  <div class="field col2 abs" style="top:3427px">Do you have a 4-year degree?</div>
  <div class="field col3 abs" style="top:3427px">The time zone you're in</div>
  <div class="field textarea abs">Enter Your Question</div>
  <div class="send-btn abs">SEND</div>
</section>

<footer class="site-footer abs"></footer>
<h4 class="f-head abs" style="left:118px">About Brightdesk Learning</h4>
<div class="f-rule abs" style="left:118px"></div>
<p class="f-text abs" style="left:118px;top:3838px;width:205px">Lorem ipsum dolor sit amet, consectetur adipiscing elit, sed do eiusmod tempor magna aliqua.</p>
<p class="f-text abs" style="left:118px;top:3918px;width:205px">Morbi quis risus semper, tempus lorem efficitur erat. Morbi vel ex.</p>

<h4 class="f-head abs" style="left:361px">Quick Links</h4>
<div class="f-rule abs" style="left:361px"></div>
<ul class="f-links abs" style="left:361px;top:3838px"><li>Courses</li><li class="on">About Us</li><li>Events</li><li>Blog</li><li>Shortcodes</li></ul>
<ul class="f-links abs" style="left:462px;top:3838px"><li>Become Instructor</li><li>Terms of Use</li><li>Privacy Policy</li><li>Legal Disclaimer</li></ul>

<h4 class="f-head abs" style="left:603px">Recent Courses</h4>
<div class="f-rule abs" style="left:603px"></div>
<div class="course-thumb abs" style="left:603px;top:3843px;background:linear-gradient(135deg,#777,#bbb)" role="img" aria-label="Course thumbnail photo"></div>
<div class="course abs" style="left:683px;top:3845px;width:150px"><b>Website Framework Basics</b><small>Marta Lin, online course, six weeks</small></div>
<div class="course-thumb abs" style="left:603px;top:3930px;background:#3a3f46"></div>
<div class="course abs" style="left:683px;top:3932px;width:150px"><b>Layout Toolkit Updates</b><small>Marta Lin, online course, four weeks</small></div>

<h4 class="f-head abs" style="left:845px">Quick Contact</h4>
<div class="f-rule abs" style="left:845px"></div>
<div class="f-input abs" style="top:3848px;height:34px;line-height:34px">Your email address</div>
<div class="f-input abs" style="top:3893px;height:76px;line-height:34px">Type your message</div>
<div class="f-send abs"><svg width="33" height="26" viewBox="0 0 33 26"><path d="M11 13h11M18 9l4 4-4 4" fill="none" stroke="#fff" stroke-width="2"/></svg></div>

<div class="f-bottom abs"></div>
<p class="copyright abs">Copyright 2015. All Rights Reserved.</p>

</body>
</html>
```